HK-Steuerberatung WordPress Site fully implemented (tax advisor)

Hello!
I need a little Wordpress Site for my newly founded Tax-Advisor Company.
I am a one-man Office advising in the area of Crypto-Currency.
PLEASE only provide a Design, if you can also Implement a WP-Site afterwards on an existing Webspace.

Please find the Content and Website-Description in the attached Document

Language for the Website is German (for now)

Target Market(s)

Tax-Advisory (specialized in Crypto Currency)

Coding

Coded - Design and coding required

Number of Pages Required

5+ page

Font styles to use
Sans Serif

Requirements
Must have
• Wordpress Implementation afterwards - Details according to attached Project Information Document

```html
<!DOCTYPE html>
<html lang="de">
<head>
<meta charset="utf-8">
<title>Über mich – HK Steuerberatung</title>
<link href="https://fonts.googleapis.com/css2?family=Inter:wght@400;500;600;700&display=swap" rel="stylesheet">
<style>
:root{
  --navy:#1b2740;
  --ink:#161616;
  --footer:#282b32;
  --grey-top:#dadada;
  --white:#ffffff;
  --photo-a:#4a5670;
  --photo-b:#2f80c8;
}
*{margin:0;padding:0;box-sizing:border-box}
html,body{width:994px;height:1200px;overflow:hidden}
body{font-family:'Inter',sans-serif;color:var(--ink);background:var(--white);position:relative}
.topbar{position:absolute;left:0;top:0;width:994px;height:30px;background:var(--navy);color:var(--white);font-size:8.5px}
.topbar .social{position:absolute;left:88px;top:9px;display:flex;gap:12px}
.topbar .social span{width:13px;height:13px;border:1.6px solid var(--white);border-radius:3px;display:block}
.topbar .contact{position:absolute;top:10px;display:flex;align-items:center;gap:5px}
.header{position:absolute;left:0;top:30px;width:994px;height:84px;background:var(--white)}
.brand{position:absolute;display:flex;align-items:center;gap:8px;font-weight:700;letter-spacing:.3px}
.brand .mark{display:block;background:var(--navy)}
.header .brand{left:86px;top:19px;font-size:17px;color:var(--navy)}
.header .brand .mark{width:40px;height:46px}
.nav a{position:absolute;top:34px;font-size:12.5px;font-weight:500;color:var(--ink);text-decoration:none}
.nav a.active{color:var(--navy);border-bottom:1.5px solid var(--navy);padding-bottom:3px}
.hero{position:absolute;left:0;top:114px;width:994px;height:240px;background:linear-gradient(var(--grey-top),var(--white))}
.hero h1{position:absolute;left:0;width:994px;top:52px;text-align:center;font-size:54px;font-weight:600;letter-spacing:-.5px}
.about{position:absolute;left:132px;top:290px;width:412px;font-size:12px;line-height:18.7px}
.about p{margin-bottom:18.7px}
.btn{display:flex;align-items:center;justify-content:center;gap:10px;width:228px;height:40px;background:var(--navy);color:var(--white);border-radius:4px;font-size:12.5px;font-weight:500;margin-top:12px}
.cv{position:absolute;left:132px;width:360px;font-size:12px;line-height:18.7px}
.cv h2{font-size:12px;font-weight:600}
.photo{position:absolute;left:614px;top:294px;width:272px;height:626px;background:linear-gradient(var(--photo-a) 65%,var(--photo-b));border-radius:120px 120px 6px 6px;opacity:.85}
.footer{position:absolute;left:0;top:1057px;width:994px;height:143px;background:var(--footer);color:var(--white)}
.footer .brand{left:94px;top:33px;font-size:13.5px;color:var(--white)}
.footer .brand .mark{width:30px;height:36px;background:var(--white)}
.footer .reach{position:absolute;left:338px;top:38px;font-size:10px;font-weight:500;line-height:13px}
.footer .fnav a{position:absolute;top:54px;font-size:10px;font-weight:500;color:var(--white);text-decoration:none}
.footer .rule{position:absolute;left:88px;top:99px;width:820px;height:1px;background:#6a6e76}
.footer .copy{position:absolute;left:0;width:994px;top:112px;text-align:center;font-size:8px;font-weight:500}
</style>
</head>
<body>
<div class="topbar">
  <div class="social"><span></span><span></span></div>
  <div class="contact" style="left:686px">
    <svg width="10" height="10" viewBox="0 0 24 24"><path fill="#fff" d="M6.6 10.8a15 15 0 006.6 6.6l2.2-2.2c.3-.3.7-.4 1-.2 1.1.4 2.3.6 3.6.6.6 0 1 .4 1 1V20c0 .6-.4 1-1 1A17 17 0 013 4c0-.6.4-1 1-1h3.5c.6 0 1 .4 1 1 0 1.3.2 2.5.6 3.6.1.3 0 .7-.2 1z"/></svg>
    +43 512 400 180
  </div>
  <div class="contact" style="left:794px">
    <svg width="12" height="9" viewBox="0 0 24 18"><rect width="24" height="18" rx="2" fill="#fff"/><path d="M1 2l11 8 11-8" stroke="#1b2740" stroke-width="2" fill="none"/></svg>
    office@hk-beratung.tirol
  </div>
</div>

<header class="header">
  <div class="brand"><span class="mark"></span>HK STEUERBERATUNG</div>
  <nav class="nav">
    <a class="active" style="left:510px">HOME</a>
    <a style="left:567px">LEISTUNGEN</a>
    <a style="left:666px">ÜBER MICH</a>
    <a style="left:750px">KONTAKT</a>
    <a style="left:829px">IMPRESSUM</a>
  </nav>
</header>

<section class="hero"><h1>Über mich</h1></section>

<section class="about">
  <p><strong>Mag. Lukas Berger</strong> Ich blicke auf eine sehr umfassende Ausbildung und langjährige Berufserfahrung in der IT Branche zurück. Nach Abschluss des Wirtschaftsstudiums habe ich den klassischen Weg der Steuerberaterausbildung absolviert und bin in diesem Bereich seit über 13 Jahren beratend tätig.</p>
  <p>Durch die Kombination meines umfassenden Wissens in der IT und der Wirtschaft habe ich schon immer gerne Unternehmen mit besonderes technischen oder digitalen Geschäftsmodellen beraten. Seit mehreren Jahren bin ich privat an der Blockchaintechnologie und dem Krypto-Universum interessiert und bereits seit dem Jahre 2017 ist dieses Thema auch Teil meiner fixen Beratungsfelder in der Steuerberatung.</p>
  <a class="btn">
    <svg width="10" height="10" viewBox="0 0 10 10"><rect width="10" height="10" fill="#fff"/></svg>
    Visit ProLink Profile
    <svg width="12" height="10" viewBox="0 0 12 10"><path d="M0 5h11M7 1l4 4-4 4" stroke="#fff" stroke-width="1.3" fill="none"/></svg>
  </a>
</section>

<section class="cv" style="top:633px">
  <h2>AUSBILDUNG</h2>
  <p>2002 – HTL - Matura mit Schwerpunkt IT und Betrieblicher Organisation<br>
  2009 –Studium BWL mit Schwerpunkten Banking &amp; Finance sowie Kapitalmärkte<br>
  2012 – Buchhalter &amp; Bilanzbuchhalterprüfung<br>
  2013 – Angelobung zum Steuerberater</p>
</section>

<section class="cv" style="top:791px">
  <h2>Beruflicher Werdegang</h2>
  <p>2003 – 2009 – Selbständig tätig im IT Sektor<br>
  Seit 2009 – Beratend tätig in der Steuerberatung / Wirtschaftsprüfung in verschiedenen Kanzleien. Zuletzt in leitender Funktion bei Varentis Tirol<br>
  2022: Gründung der eigenen Kanzlei HK-Steuerberatung mit Fokus Krypto-Beratung.</p>
</section>

<div class="photo" role="img" aria-label="Porträtfoto des Steuerberaters im blauen Anzug, auf einem blauen Barhocker sitzend"></div>

<footer class="footer">
  <div class="brand"><span class="mark"></span>HK STEUERBERATUNG</div>
  <div class="reach">Email: office@hk-beratung.tirol<br>Phone : +43 512 400 180</div>
  <nav class="fnav">
    <a style="left:568px">HOME</a>
    <a style="left:623px">LEISTUNGEN</a>
    <a style="left:704px">ÜBER MICH</a>
    <a style="left:778px">KONTAKT</a>
    <a style="left:846px">IMPRESSUM</a>
  </nav>
  <div class="rule"></div>
  <div class="copy">Copyright ©&nbsp; 2022 HK STEUERBERATUNG</div>
</footer>
</body>
</html>
```